TPR Letterhead

We need a letterhead design that will be able to be used on all marketing products (letterhead, mail chimp, envelops, business cards, etc.) We are a law firm specializing primarily in transportation law but offer a wide range of services to our clients. We would like the design to be modern, simple, and professional. Our colors are black and gold, however, we've incorporated dark gray and white on other marketing products such as our website.

```html
<!DOCTYPE html>
<html lang="en">
<head>
<meta charset="utf-8">
<title>TPR Law Group – Business Cards</title>
<link rel="stylesheet" href="https://fonts.googleapis.com/css2?family=Cinzel:wght@400&family=Roboto:wght@400;700&display=swap">
<style>
  :root {
    --ink: #0a0a0a;
    --gold: #a8895a;
    --paper: #ffffff;
    --text: #2b2b2b;
    --stage: #eeece9;
  }
  * { margin: 0; padding: 0; box-sizing: border-box; }
  html, body { width: 1200px; height: 961px; overflow: hidden; background: var(--stage); }
  .stage { position: relative; width: 1200px; height: 961px; }

  .card {
    position: absolute;
    width: 530px;
    height: 303px;
    box-shadow: 0 2px 6px rgba(0,0,0,.12);
  }

  /* Front */
  .card--front { left: 70px; top: 120px; background: var(--ink); }
  .card--front .wordmark {
    position: absolute; inset: 0;
    display: flex; flex-direction: column; align-items: center; justify-content: center;
    font-family: 'Cinzel', serif; font-weight: 400; color: var(--paper);
  }
  .wordmark__name { font-size: 62px; letter-spacing: 4px; line-height: 1; }
  .wordmark__sub { font-size: 22px; letter-spacing: 7px; margin-top: 8px; }

  /* Back */
  .card--back { left: 600px; top: 500px; background: var(--paper); }
  .card--back .wordmark {
    position: absolute; right: 46px; top: 34px;
    font-family: 'Cinzel', serif; font-weight: 400; color: var(--ink);
    text-align: center;
  }
  .card--back .wordmark__name { font-size: 40px; letter-spacing: 3px; }
  .card--back .wordmark__sub { font-size: 14px; letter-spacing: 5px; margin-top: 6px; }

  .rule {
    position: absolute; left: 250px; right: 40px; top: 152px;
    height: 1.5px; background: var(--gold);
  }

  .person { position: absolute; left: 34px; top: 138px; font-family: 'Roboto', sans-serif; }
  .person__name { color: var(--gold); font-weight: 700; font-size: 19px; letter-spacing: .3px; }
  .person__role { color: var(--text); font-weight: 700; font-size: 14px; margin-top: 2px; }

  .contact { list-style: none; margin-top: 10px; }
  .contact li {
    display: flex; align-items: center; gap: 8px;
    color: var(--text); font-size: 15px; line-height: 22px;
  }
  .contact svg { width: 13px; height: 13px; flex: none; }

  .address {
    position: absolute; right: 30px; top: 196px;
    font-family: 'Roboto', sans-serif; font-size: 14px; color: var(--text);
    text-align: right; line-height: 19px;
  }

  .band { position: absolute; bottom: 0; height: 9px; }
  .band--ink { left: 0; width: 320px; background: var(--ink); }
  .band--gold { left: 328px; right: 0; background: var(--gold); bottom: 5px; }
</style>
</head>
<body>
<main class="stage">

  <section class="card card--front" aria-label="Business card front">
    <div class="wordmark">
      <span class="wordmark__name">TPR</span>
      <span class="wordmark__sub">LAW GROUP</span>
    </div>
  </section>

  <section class="card card--back" aria-label="Business card back">
    <div class="wordmark">
      <div class="wordmark__name">TPR</div>
      <div class="wordmark__sub">LAW GROUP</div>
    </div>

    <div class="rule"></div>

    <div class="person">
      <div class="person__name">DANIEL HARROW</div>
      <div class="person__role">Managing Director</div>
      <ul class="contact">
        <li>
          <svg viewBox="0 0 16 16" aria-hidden="true"><path fill="#a8895a" d="M2 4c0-1 1-2 2-2h8c1 0 2 1 2 2v1h-3V4H5v1H2zM4 7h8l2 6H2z"/></svg>
          +15550142733
        </li>
        <li>
          <svg viewBox="0 0 16 16" aria-hidden="true"><rect x="1" y="3" width="14" height="10" fill="#a8895a"/><path d="M1 3l7 6 7-6" fill="none" stroke="#fff" stroke-width="1.3"/></svg>
          daniel@tprlaw.com
        </li>
        <li>
          <svg viewBox="0 0 16 16" aria-hidden="true"><circle cx="8" cy="8" r="6.5" fill="none" stroke="#a8895a" stroke-width="1.5"/><path d="M1.5 8h13M8 1.5c-3 3-3 10 0 13M8 1.5c3 3 3 10 0 13" fill="none" stroke="#a8895a" stroke-width="1.2"/></svg>
          www.tprlaw.com
        </li>
      </ul>
    </div>

    <address class="address" style="font-style:normal">
      48 Cedar Crest Lane,<br>
      Maple Ridge, ON L5T 3K8
    </address>

    <div class="band band--ink"></div>
    <div class="band band--gold"></div>
  </section>

</main>
</body>
</html>
```